Powerpoint template and Word template FundLantern™ a crowdfunding business

We need powerpoint and word templates for our business. its a crowdfunding business providing information to investors as well as engaging entrepreneurs.

The logo is already designed and we have business cards for this as well. The files for these are attached and we are looking for a professional image for our presentation style.

Target Market(s)

Investors, HNWI and Entrepreneurs

Industry/Entity Type

Financial Service

Requirements
Must have
• Powerpoint and Word templates

```html
<!DOCTYPE html>
<html lang="en">
<head>
<meta charset="utf-8">
<title>FundLantern™ — Presentation Title Slide</title>
<link href="https://fonts.googleapis.com/css2?family=Arimo:wght@400;700&display=swap" rel="stylesheet">
<style>
  :root {
    --frame-grey: #cccccc;
    --slide-white: #ffffff;
    --brand-blue: #0b6bb8;
    --brand-green: #0b9444;
    --tint-green: #d7eee1;
  }
  * { margin: 0; padding: 0; box-sizing: border-box; }
  html, body {
    width: 1200px;
    height: 942px;
    overflow: hidden;
    background: var(--frame-grey);
    font-family: "Arimo", Arial, sans-serif;
  }
  .slide {
    position: absolute;
    left: 52px;
    top: 60px;
    width: 1096px;
    height: 822px;
    background: var(--slide-white);
    overflow: hidden;
  }
  .backdrop-ring {
    position: absolute;
    left: 0;
    top: 0;
    width: 1096px;
    height: 822px;
  }
  .brand {
    position: absolute;
    left: 56px;
    top: 78px;
    display: flex;
    align-items: center;
    gap: 18px;
  }
  .brand-dot {
    width: 70px;
    height: 70px;
    border-radius: 50%;
    background: var(--brand-green);
  }
  .brand-name {
    font-size: 46px;
    font-weight: 700;
    color: var(--brand-blue);
    letter-spacing: 1px;
  }
  .title-block {
    position: absolute;
    left: 61px;
    top: 440px;
    width: 600px;
    text-align: center;
  }
  .title {
    font-size: 39px;
    font-weight: 700;
    color: var(--brand-blue);
    line-height: 48px;
  }
  .subheading {
    font-size: 39px;
    font-weight: 400;
    color: var(--brand-green);
    line-height: 48px;
  }
</style>
</head>
<body>
  <main class="slide">
    <svg class="backdrop-ring" viewBox="0 0 1096 822" aria-hidden="true">
      <circle cx="818" cy="476" r="318" fill="none" stroke="var(--tint-green)" stroke-width="57"/>
    </svg>

    <div class="brand">
      <span class="brand-dot"></span>
      <span class="brand-name">FundLantern™</span>
    </div>

    <div class="title-block">
      <h1 class="title">Presentation Title goes here</h1>
      <h2 class="subheading">Subheading Goes Here</h2>
    </div>
  </main>
</body>
</html>
```